HVAC company business card design

We need a business card design for a HVAC company. The design must look professional. Both sides will be used. The total data to be on the business card is
Name
Position
Email
Direct Phone/Moile Phone
Company Contacts /Address, Phone, Fax, web)
All data will be submit once the design is confirmed. For generic purposes use;
Emre Toksoy
Managing Director
+902324815263 (Mobile)
4712 Sokak No: 9 KBSE Yenikent IZMIR TURKEY
Tel: +902324815263 Fax : +902324815269
www.luvon.com.tr

Target Market(s)

HVAC

Industry/Entity Type

Business

Contact Information for Business Card

The total data to be on the business card is
Name
Position
Email
Direct Phone/Moile Phone
Emre Toksoy
Managing Director
+902324815263 (Mobile)
www.luvon.com.tr
The BC will use both sides of the card. The front will include the full logo and the details for the business card holder. The business card can be divided into vertical/horizontal or to a special shape. The common data like the company address/phone/fax should be indicated elsewehere. The back can contain some part or the whole logo and must contain the web address.

Font styles to use
Serif
Sans Serif

Colors
0355a3
cfdfed

Requirements
Should not have
• Please be careful with the fonts, it shouldnt be too small or too big and must not interfere with the logo fonts. If you need to use a curvy shape please do not use as the logo is already curvy or use the curves from the logo (if it looks good, otherwise forget it)
• We are not in favor of pictograms, only if they are perfect use them.

```html
<!DOCTYPE html>
<html lang="en">
<head>
<meta charset="utf-8">
<title>LUVON – Business Card</title>
<link rel="stylesheet" href="https://fonts.googleapis.com/css2?family=Montserrat:wght@400;500;700&display=swap">
<style>
  :root {
    --backdrop: #2b2c2f;
    --card-slate: #454e6b;
    --brand-blue: #3a6bbf;
    --pale-blue: #cfdfed;
    --white: #ffffff;
    --soft-text: #e4e8f2;
  }
  * { box-sizing: border-box; margin: 0; padding: 0; }
  html, body {
    width: 1200px; height: 900px; overflow: hidden;
    background: var(--backdrop);
    font-family: "Montserrat", Arial, sans-serif;
  }
  .canvas { position: relative; width: 1200px; height: 900px; }

  .card {
    position: absolute;
    width: 560px; height: 320px;
    background: var(--card-slate);
    border-radius: 18px;
    overflow: hidden;
    box-shadow: 0 18px 40px rgba(0,0,0,.45);
  }
  .card--back { left: 90px; top: 90px; }
  .card--front { left: 550px; top: 490px; }

  /* Back side */
  .back-mark {
    position: absolute; left: 0; right: 0; top: 88px;
    display: flex; align-items: center; justify-content: center; gap: 18px;
  }
  .mark-dot {
    width: 46px; height: 46px; border-radius: 50%;
    background: var(--brand-blue);
  }
  .back-name {
    font-size: 56px; font-weight: 700; letter-spacing: 4px;
    color: var(--white);
  }
  .back-web {
    position: absolute; left: 0; right: 0; bottom: 54px;
    text-align: center; color: var(--soft-text);
    font-size: 19px; letter-spacing: 1.5px;
  }

  /* Front side */
  .front-swoosh { position: absolute; inset: 0; }
  .front-brand {
    position: absolute; left: 34px; top: 64px;
    display: flex; align-items: center; gap: 12px;
  }
  .front-brand .mark-dot { width: 30px; height: 30px; }
  .front-brand-name {
    font-size: 36px; font-weight: 700; letter-spacing: 3px; color: var(--white);
  }
  .holder {
    position: absolute; left: 150px; top: 118px;
    color: var(--white);
  }
  .holder-name { font-size: 19px; font-weight: 700; line-height: 1.2; }
  .holder-role { font-size: 11px; letter-spacing: 1px; margin-bottom: 8px; }
  .holder-address { font-size: 11.5px; line-height: 1.35; margin-bottom: 6px; }
  .contact-list { list-style: none; font-size: 11.5px; line-height: 1.45; }
  .contact-list li { display: flex; align-items: center; gap: 8px; }
  .contact-list svg { width: 10px; height: 10px; flex: none; }
</style>
</head>
<body>
<div class="canvas">

  <section class="card card--back">
    <div class="back-mark">
      <span class="mark-dot"></span>
      <span class="back-name">LUVON</span>
    </div>
    <p class="back-web">www.luvon.com.tr</p>
  </section>

  <section class="card card--front">
    <svg class="front-swoosh" viewBox="0 0 560 320" aria-hidden="true">
      <path d="M230 0 H560 V250 C540 120 450 30 230 0 Z" fill="var(--brand-blue)"/>
      <path d="M232 6 C455 38 528 130 544 262" fill="none" stroke="var(--white)" stroke-width="16"/>
    </svg>

    <div class="front-brand">
      <span class="mark-dot"></span>
      <span class="front-brand-name">LUVON</span>
    </div>

    <div class="holder">
      <p class="holder-name">Emre Toksoy</p>
      <p class="holder-role">MANAGING DIRECTOR</p>
      <p class="holder-address">4712 Sokak No: 9 KBSE Yenikent<br>IZMIR TURKEY</p>
      <ul class="contact-list">
        <li>
          <svg viewBox="0 0 10 10"><rect x="2.5" y="0.5" width="5" height="9" rx="1" fill="none" stroke="#fff"/></svg>
          +902324815263
        </li>
        <li>
          <svg viewBox="0 0 10 10"><path d="M2 1 L4 1 L4.6 3.2 L3.4 4 Q4.5 6 6 6.6 L6.8 5.4 L9 6 L9 8 Q5 9.5 1 3 Z" fill="#fff"/></svg>
          +902324815263
        </li>
        <li>
          <svg viewBox="0 0 10 10"><rect x="1" y="3" width="8" height="5" fill="#fff"/><rect x="2.5" y="1" width="5" height="2.5" fill="none" stroke="#fff"/></svg>
          +902324815269
        </li>
        <li>
          <svg viewBox="0 0 10 10"><rect x="0.5" y="2" width="9" height="6" fill="none" stroke="#fff"/><path d="M0.5 2 L5 5.5 L9.5 2" fill="none" stroke="#fff"/></svg>
          info@luvon.com.tr
        </li>
        <li>
          <svg viewBox="0 0 10 10"><circle cx="5" cy="5" r="4.3" fill="none" stroke="#fff"/><ellipse cx="5" cy="5" rx="1.8" ry="4.3" fill="none" stroke="#fff"/><path d="M0.7 5 H9.3" stroke="#fff"/></svg>
          www.luvon.com.tr
        </li>
      </ul>
    </div>
  </section>

</div>
</body>
</html>
```